Business Card for Multi-Brand Sportswear Company

We are looking for a business card which represents our company and the multiple brands within it.

The company: Kelt Athletic (LTD)
The brands: Kelt, PawaLuni, VerdantFlex, Grit and Gale

Employees using these cards would be representing Kelt Athletic, rather than any of the individual brands. You will see a current design within the uploaded files, to give some inspiration. The actual text of the brands is not necessary, but the logos should be on there is some format.

Our creative minds on this are stretched, so we are looking for someone to make this their own, and show us what a good business card should look like.

We may like to get these printed with spot gloss, so keep that in mind with your designs.

www.keltathletic.co.uk

Industry/Entity Type

Business

Contact Information for Business Card

Tom Hollingsworth-Pryce
Operations Manager
(+44) 1632 960 418
Tom@keltathletic.co.uk
www.keltathletic.co.uk

Font styles to use
Sans Serif
Other font styles liked:
• Eurostile

Colors
ffffff

Requirements
Nice to have
• Dark (black) background

```html
<!DOCTYPE html>
<html lang="en">
<head>
<meta charset="utf-8">
<title>Kelt Athletic – Business Card</title>
<link rel="stylesheet" href="https://fonts.googleapis.com/css2?family=Saira:wght@400;500;600&display=swap">
<style>
  :root {
    --backdrop: #e4e4e4;
    --card-dark: #1a1a1a;
    --card-light: #ffffff;
    --ink: #111111;
    --ink-soft: #333333;
    --accent: #e3242b;
    --band: #0d0d0d;
  }
  * { box-sizing: border-box; margin: 0; padding: 0; }
  html, body {
    width: 1200px; height: 586px; overflow: hidden;
    background: var(--backdrop);
    font-family: "Saira", "Helvetica Neue", Arial, sans-serif;
  }
  .canvas { position: relative; width: 1200px; height: 586px; }

  .card {
    position: absolute; top: 128px;
    width: 502px; height: 301px; overflow: hidden;
  }
  .card--front { left: 65px; background: var(--card-dark); }
  .card--back  { left: 608px; background: var(--card-light); }

  .brand-lockup { position: absolute; left: 0; right: 0; text-align: center; line-height: 1; }
  .brand-lockup__name { font-weight: 500; letter-spacing: 0.02em; }
  .brand-lockup__tagline { font-weight: 400; letter-spacing: 0.22em; }

  .card--front .brand-lockup { top: 122px; color: var(--card-light); }
  .card--front .brand-lockup__name { font-size: 42px; }
  .card--front .brand-lockup__tagline { font-size: 10px; margin-top: 8px; }

  .card--back .brand-lockup { top: 36px; color: var(--ink); }
  .card--back .brand-lockup__name { font-size: 24px; }
  .card--back .brand-lockup__tagline { font-size: 6.5px; margin-top: 4px; color: var(--ink-soft); }

  .person { position: absolute; left: 25px; top: 130px; }
  .person__name { font-size: 17px; font-weight: 600; color: var(--ink); line-height: 1.2; }
  .person__role { font-size: 12px; color: var(--ink-soft); margin-top: 3px; }

  .contact-list { position: absolute; left: 25px; top: 203px; list-style: none; }
  .contact-list__item {
    display: flex; align-items: center; gap: 9px;
    height: 24px; font-size: 11.5px; color: var(--ink-soft);
  }
  .contact-list__icon { width: 13px; height: 13px; fill: var(--accent); flex: none; }

  .address {
    position: absolute; right: 26px; top: 198px; text-align: right;
    font-size: 13px; font-weight: 600; color: var(--ink); line-height: 17px;
    font-style: normal;
  }

  .brand-row {
    position: absolute; right: 26px; top: 246px;
    display: flex; align-items: center; gap: 11px; list-style: none;
  }
  .brand-row__item {
    display: flex; align-items: center; gap: 4px;
    font-size: 11px; font-weight: 600; color: var(--ink-soft);
  }
  .brand-row__dot { width: 8px; height: 8px; background: var(--accent); flex: none; }

  .card__band { position: absolute; left: 0; right: 0; bottom: 0; height: 14px; background: var(--band); }
</style>
</head>
<body>
<main class="canvas">

  <section class="card card--front" aria-label="Card front">
    <div class="brand-lockup">
      <div class="brand-lockup__name">KELT ATHLETIC</div>
      <div class="brand-lockup__tagline">PERFORMANCE WEAR</div>
    </div>
  </section>

  <section class="card card--back" aria-label="Card back">
    <div class="brand-lockup">
      <div class="brand-lockup__name">KELT ATHLETIC</div>
      <div class="brand-lockup__tagline">PERFORMANCE WEAR</div>
    </div>

    <div class="person">
      <div class="person__name">Tom Hollingsworth-Pryce</div>
      <div class="person__role">Operations Manager</div>
    </div>

    <ul class="contact-list">
      <li class="contact-list__item">
        <svg class="contact-list__icon" viewBox="0 0 16 16" aria-hidden="true">
          <path d="M2 6c0-2 3-3.5 6-3.5S14 4 14 6v1.2h-3V5.8H5v1.4H2z"/>
          <path d="M4 8h8l1.5 5.5h-11z"/>
        </svg>
        <span>(+44) 1632 960 418</span>
      </li>
      <li class="contact-list__item">
        <svg class="contact-list__icon" viewBox="0 0 16 16" aria-hidden="true">
          <path d="M1 3.5h14v9H1z"/>
          <path d="M1.5 4l6.5 5 6.5-5" fill="none" stroke="#fff" stroke-width="1.3"/>
        </svg>
        <span>Tom@keltathletic.co.uk</span>
      </li>
      <li class="contact-list__item">
        <svg class="contact-list__icon" viewBox="0 0 16 16" aria-hidden="true">
          <circle cx="8" cy="8" r="7"/>
          <path d="M1 8h14M8 1c-2.5 2-2.5 12 0 14M8 1c2.5 2 2.5 12 0 14" fill="none" stroke="#fff" stroke-width="1.1"/>
        </svg>
        <span>www.keltathletic.co.uk</span>
      </li>
    </ul>

    <address class="address">
      Elm Park, Ashby<br>
      Thornbury, ZZ9 4QX
    </address>

    <ul class="brand-row" aria-label="Group brands">
      <li class="brand-row__item">Kelt</li>
      <li class="brand-row__item"><span class="brand-row__dot"></span>PawaLuni</li>
      <li class="brand-row__item">VerdantFlex</li>
      <li class="brand-row__item">Grit and Gale</li>
    </ul>

    <div class="card__band"></div>
  </section>

</main>
</body>
</html>
```